I have a logo and need to design the business card and stationery.
Updates

The uploaded logo image named as GREYHAVEN CONSTRUCTION which is to be replaced to GREYHAVEN CONTRACTS. Kindly add below details and submit the designs- Company name- Greyhaven Engineering Contracts LLP Name & Post- Kunal Mehra (Designated Partner) Address- Block No.317, Wing C, Tulsi Trade Plaza, Lokhand Marg, Varun Industrial Park, Goregaon(E), Mumbai - 400 063 Contact- +91 97410 58723 Email- kunalmehra@examplemail.com Website- www.greyhavencontracts.example Contact for Letterhead- +91-22-28145597

Hi Tanvir Rahman, We are liking your Design #41927506. We have suggested some changes which are mentioned in feedback. Kindly revert with it asap to finalize this design.

Colors

Designer to choose colors to be used in the design.

```html
<!DOCTYPE html>
<html lang="en">
<head>
<meta charset="utf-8">
<title>Greyhaven Contracts — Business Card</title>
<link href="https://fonts.googleapis.com/css2?family=Exo+2:wght@400;600;700&display=swap" rel="stylesheet">
<style>
  :root {
    --backdrop: #e6e6e6;
    --card-white: #ffffff;
    --card-dark: #333333;
    --mark-grey: #4a4a4a;
    --ink: #2f2f2f;
    --text-light: #ffffff;
  }
  * { margin: 0; padding: 0; box-sizing: border-box; }
  html, body {
    width: 1133px; height: 1200px; overflow: hidden;
    background: var(--backdrop);
    font-family: "Exo 2", sans-serif;
  }
  .canvas { position: relative; width: 1133px; height: 1200px; }

  .card { position: absolute; background: var(--card-white); }
  .card-front { left: 192px; top: 139px; width: 734px; height: 417px; }
  .card-back  { left: 196px; top: 641px; width: 727px; height: 416px; }

  .front-panel {
    position: absolute; left: 16px; top: 15px; right: 17px; bottom: 15px;
    background: var(--card-dark);
  }
  .contact-block { position: absolute; left: 33px; top: 79px; color: var(--text-light); }
  .person-name { font-size: 25px; font-weight: 700; letter-spacing: 0.3px; line-height: 1; }
  .person-role { font-size: 15.5px; font-weight: 400; margin-top: 4px; }
  .address { font-size: 16.5px; line-height: 21px; margin-top: 23px; }
  .contact-list { list-style: none; margin-top: 12px; font-size: 16.5px; line-height: 21px; }
  .contact-list li { display: flex; align-items: center; gap: 8px; }
  .contact-list svg { width: 14px; height: 14px; fill: var(--text-light); flex: none; }

  .front-brand {
    position: absolute; left: 351px; top: 38px; width: 311px; height: 312px;
    display: flex; flex-direction: column; align-items: center; justify-content: center; gap: 22px;
  }
  .brand-square-large { width: 70px; height: 70px; background: var(--text-light); }
  .front-brand-name {
    color: var(--text-light); font-size: 40px; font-weight: 700; letter-spacing: 1px;
  }

  .back-brand {
    position: absolute; left: 0; right: 0; top: 120px;
    display: flex; flex-direction: column; align-items: center;
  }
  .brand-square { width: 106px; height: 106px; background: var(--ink); }
  .back-brand-name {
    margin-top: 16px; color: var(--ink); font-size: 34px; font-weight: 700;
    letter-spacing: 2px; line-height: 30px; text-align: center;
  }
</style>
</head>
<body>
<main class="canvas">
  <section class="card card-front">
    <div class="front-panel">
      <div class="contact-block">
        <h1 class="person-name">DANIEL HARLOW</h1>
        <p class="person-role">President</p>
        <address class="address" style="font-style:normal">
          4129 Juniper Row<br>Fairbanks<br>Alaska 36218
        </address>
        <ul class="contact-list">
          <li><svg viewBox="0 0 24 24"><path d="M6.6 10.8a15.1 15.1 0 0 0 6.6 6.6l2.2-2.2c.3-.3.7-.4 1-.2 1.1.4 2.3.6 3.6.6.6 0 1 .4 1 1V20c0 .6-.4 1-1 1A17 17 0 0 1 3 4c0-.6.4-1 1-1h3.5c.6 0 1 .4 1 1 0 1.3.2 2.5.6 3.6.1.3 0 .7-.2 1z"/></svg>369-480-1273</li>
          <li><svg viewBox="0 0 24 24"><path d="M7 1h10a2 2 0 0 1 2 2v18a2 2 0 0 1-2 2H7a2 2 0 0 1-2-2V3a2 2 0 0 1 2-2zm0 3v14h10V4zm5 15.5a1 1 0 1 0 0 2 1 1 0 0 0 0-2z"/></svg>369-627-3945</li>
          <li><svg viewBox="0 0 24 24"><path d="M2 6h20v12H2zm2 1.5 8 5.5 8-5.5z"/></svg>name@greyhaven.example</li>
          <li><svg viewBox="0 0 24 24"><path d="M12 2a10 10 0 1 0 0 20 10 10 0 0 0 0-20zm-1 17.9A8 8 0 0 1 4.2 10L9 14.8v1a2 2 0 0 0 2 2zm6.9-2.5A2 2 0 0 0 16 16h-1v-3a1 1 0 0 0-1-1H8v-2h2a1 1 0 0 0 1-1V7h2a2 2 0 0 0 2-2v-.4a8 8 0 0 1 2.9 12.8z"/></svg>www.greyhaven.example</li>
        </ul>
      </div>
      <div class="front-brand">
        <div class="brand-square-large"></div>
        <span class="front-brand-name">GREYHAVEN</span>
      </div>
    </div>
  </section>

  <section class="card card-back">
    <div class="back-brand">
      <div class="brand-square"></div>
      <p class="back-brand-name">GREYHAVEN<br>CONTRACTS</p>
    </div>
  </section>
</main>
</body>
</html>
```